Icons für Tischtennistraining
Es war der einzige designer welcher etwas wirklich spezielles geliefert hat. Anpassungswünsche wurden sofort verstanden und treffend umgesetzt. Vielen Dank für die Zusammenarbeit
Zielgruppe
Ballwechselhalle.ch ist ein gemeinnütziger Verein mit einem einzigartigen Gesundheits- und Inklusionsangebot:
Menschen mit Parkinson, Multipler Sklerose, kognitiven Einschränk­ungen, im Rollstuhl und ältere Menschen trainieren gemeinsam mit Menschen ohne Einschränkungen.
Aufgabenstellung
Wir brauchen 5 Icons für unsere 5 Kernelemente welche mit den Trainings gefördert werden.
Diese sollen ins Farbkonzept des bestehenden Logos passen. Die Farbe der Icons soll als Erkennung des Kernelementes dienen.
Die Icons sollen das Thema des entsprechendes Kernelementes grafisch ausdrücken. Die Icons auf der Website erfüllen den zweck an und für sich nicht schlecht und können einen Anhaltspunkt geben. Die Farbwahl ist den Designern überlassen müssen aber mit dem bestehenden Logo harmonieren.
Wichtig: Die Kernthemen sind eine Vorgabe. Ebenfalls muss jedes Icon eine eigen Farbe haben, diese wird für Content innerhalb des Themas als führende Farbe verwendet. Es müssen keineswegs Strichmännchen verwendet werden. Das Icon / Symbol soll dass Thema verständlich symbolisieren. wir sind offen für Ideen.
Wir sind auf die Ideen sehr gespannt.

```html
<!DOCTYPE html>
<html lang="de">
<head>
<meta charset="utf-8">
<title>Ballwechselhalle.ch – Tischtennis als Gesundheitssport</title>
<link rel="stylesheet" href="https://fonts.googleapis.com/css2?family=Arimo:wght@400;700&display=swap">
<style>
  :root {
    --pink: #e0237c;
    --purple: #9a3fc4;
    --violet: #5b3aa8;
    --blue: #1766c0;
    --teal: #17b2b8;
    --cyan: #1ec3d2;
    --heading: #1a6fb5;
    --text: #3b3b3b;
    --muted: #666;
    --map: #f3f3f1;
    --side: #efeee9;
    --white: #ffffff;
  }
  * { box-sizing: border-box; margin: 0; padding: 0; }
  html, body { width: 1200px; height: 848px; overflow: hidden; background: var(--white); }
  body { position: relative; font-family: "Arimo", Arial, sans-serif; color: var(--text); }

  .site-header { position: absolute; left: 0; top: 0; width: 1200px; height: 100px; }
  .brand { position: absolute; left: 161px; top: 45px; display: flex; align-items: center; gap: 9px; }
  .brand-dot { width: 26px; height: 26px; border-radius: 50%; background: var(--pink); }
  .brand-name { font-size: 18px; font-weight: 700; color: var(--blue); }

  .main-nav a { position: absolute; top: 52px; font-size: 14px; color: #222; text-decoration: none; }
  .cta-trial {
    position: absolute; left: 923px; top: 43px; width: 160px; height: 34px;
    border-radius: 8px;
    background: linear-gradient(90deg, var(--pink), var(--purple));
    color: var(--white); font-size: 15px; font-weight: 700;
    display: flex; align-items: center; justify-content: center; letter-spacing: .3px;
  }

  .hero {
    position: absolute; left: 144px; top: 101px; width: 956px; height: 362px;
    background: linear-gradient(160deg, #8b6e63 0%, #b6a39b 35%, #6a4e66 65%, #3d3350 100%);
  }
  .hero-note {
    position: absolute; left: 900px; top: 132px; width: 120px;
    font-size: 11px; font-weight: 700; color: var(--white); text-align: center; line-height: 1.25;
  }
  .hero-arrow { position: absolute; left: 960px; top: 82px; }
  .hero-title {
    position: absolute; left: 144px; top: 294px; width: 956px; text-align: center;
    color: var(--white); font-size: 20px; font-weight: 700; line-height: 1.2;
    text-shadow: 0 1px 4px rgba(0,0,0,.45);
  }
  .hero-cta {
    position: absolute; left: 510px; top: 356px; width: 221px; height: 34px; border-radius: 6px;
    background: var(--cyan); color: var(--white); font-size: 13px; font-weight: 700;
    display: flex; align-items: center; justify-content: center;
  }

  .goals-band { position: absolute; left: 124px; top: 463px; width: 996px; height: 100px; background: var(--white); }
  .goal-card {
    position: absolute; top: 437px; width: 152px; height: 104px; border-radius: 14px;
    background: var(--white); box-shadow: 0 6px 14px rgba(0,0,0,.22);
    display: flex; align-items: center; gap: 4px; padding-left: 6px;
  }
  .goal-icon { flex: none; width: 40px; height: 50px; }
  .goal-label { font-size: 13px; font-weight: 700; line-height: 1.1; letter-spacing: -.2px; }
  .goal-balance { left: 180px; color: var(--pink); }
  .goal-mobility { left: 366px; color: var(--purple); }
  .goal-energy { left: 553px; color: var(--violet); }
  .goal-focus { left: 738px; color: var(--blue); }
  .goal-community { left: 925px; color: var(--teal); }

  .why-photo {
    position: absolute; left: 185px; top: 589px; width: 418px; height: 259px;
    background: linear-gradient(180deg, #cfd2d4 0%, #9aa2ab 45%, #3e6fb3 75%, #2b4f8a 100%);
  }
  .why-map { position: absolute; left: 603px; top: 577px; width: 440px; height: 271px; background: var(--map); }
  .why-title { position: absolute; left: 618px; top: 588px; font-size: 19px; font-weight: 700; color: var(--heading); }
  .why-list { list-style: none; position: absolute; left: 620px; top: 626px; width: 300px; }
  .why-list li { position: relative; padding-left: 17px; font-size: 13px; line-height: 21px; color: var(--muted); height: 75px; }
  .why-list svg { position: absolute; left: 0; top: 8px; }

  .side-panel { position: absolute; left: 1143px; top: 567px; width: 57px; height: 281px; background: var(--side); }
</style>
</head>
<body>
  <header class="site-header">
    <div class="brand"><span class="brand-dot"></span><span class="brand-name">Ballwechselhalle.ch</span></div>
    <nav class="main-nav">
      <a style="left:412px">Deine Ziele</a>
      <a style="left:514px">Trainings</a>
      <a style="left:603px">Standorte</a>
      <a style="left:695px">Warum Tischtennis?</a>
      <a style="left:858px">Kontakt</a>
    </nav>
    <div class="cta-trial">PROBETRAINING</div>
  </header>

  <section class="hero" role="img" aria-label="Gruppenfoto: fröhliche Trainingsgruppe mit Tischtennisschlägern in einer Turnhalle"></section>
  <svg class="hero-arrow" width="30" height="46" viewBox="0 0 30 46" aria-hidden="true">
    <path d="M14 44 C4 34 6 18 16 4" fill="none" stroke="var(--pink)" stroke-width="1.6"/>
    <path d="M10 8 L16 3 L19 10" fill="none" stroke="var(--pink)" stroke-width="1.6"/>
  </svg>
  <p class="hero-note">Jetzt kostenloses Probetraining</p>
  <h1 class="hero-title">Tischtennis als Gesundheitssport<br>Training für Körper, Geist &amp; Gemeinschaft</h1>
  <div class="hero-cta">JETZT UNTERSTÜTZEN!</div>

  <div class="goals-band"></div>

  <div class="goal-card goal-balance">
    <svg class="goal-icon" viewBox="0 0 40 50" role="img" aria-label="Icon Gleichgewicht: Waage im Lot">
      <path d="M20 14 L20 42" stroke="currentColor" stroke-width="3.5" stroke-linecap="round"/>
      <path d="M6 16 L34 16" stroke="currentColor" stroke-width="3.5" stroke-linecap="round"/>
      <circle cx="20" cy="9" r="4" fill="currentColor"/>
      <path d="M2 28 L6 17 L10 28 Z M30 28 L34 17 L38 28 Z" fill="currentColor"/>
      <path d="M11 45 L29 45" stroke="currentColor" stroke-width="4" stroke-linecap="round"/>
    </svg>
    <span class="goal-label">Gleichgewicht<br>verbessern</span>
  </div>
  <div class="goal-card goal-mobility">
    <svg class="goal-icon" viewBox="0 0 40 50" role="img" aria-label="Icon Beweglichkeit: geschwungene Pfeile">
      <path d="M8 38 C8 18 18 10 32 10" fill="none" stroke="currentColor" stroke-width="4" stroke-linecap="round"/>
      <path d="M27 4 L34 10 L27 16" fill="none" stroke="currentColor" stroke-width="4" stroke-linecap="round" stroke-linejoin="round"/>
      <path d="M32 22 C32 36 24 42 12 44" fill="none" stroke="currentColor" stroke-width="4" stroke-linecap="round"/>
      <path d="M16 38 L10 44 L17 48" fill="none" stroke="currentColor" stroke-width="4" stroke-linecap="round" stroke-linejoin="round"/>
    </svg>
    <span class="goal-label">Beweglichkeit<br>fördern</span>
  </div>
  <div class="goal-card goal-energy">
    <svg class="goal-icon" viewBox="0 0 40 50" role="img" aria-label="Icon Energie: Blitz">
      <path d="M24 2 L6 28 L18 28 L14 48 L34 19 L22 19 Z" fill="currentColor"/>
    </svg>
    <span class="goal-label">Energie<br>tanken</span>
  </div>
  <div class="goal-card goal-focus">
    <svg class="goal-icon" viewBox="0 0 40 50" role="img" aria-label="Icon Konzentration: Zielscheibe">
      <circle cx="20" cy="25" r="17" fill="none" stroke="currentColor" stroke-width="3.5"/>
      <circle cx="20" cy="25" r="10" fill="none" stroke="currentColor" stroke-width="3.5"/>
      <circle cx="20" cy="25" r="4" fill="currentColor"/>
    </svg>
    <span class="goal-label">Konzentration<br>stärken</span>
  </div>
  <div class="goal-card goal-community">
    <svg class="goal-icon" viewBox="0 0 40 50" role="img" aria-label="Icon Gemeinschaft: verbundene Kreise">
      <path d="M8 34 L20 14 L32 34 Z" fill="none" stroke="currentColor" stroke-width="3"/>
      <circle cx="20" cy="14" r="7" fill="currentColor"/>
      <circle cx="8" cy="34" r="7" fill="currentColor"/>
      <circle cx="32" cy="34" r="7" fill="currentColor"/>
    </svg>
    <span class="goal-label">Gemeinschaft<br>erleben</span>
  </div>

  <div class="why-photo" role="img" aria-label="Foto: Spielerin im Rollstuhl am Tischtennistisch"></div>
  <div class="why-map" role="img" aria-label="Karte der Trainingsstandorte"></div>
  <h2 class="why-title">Warum Tischtennis?</h2>
  <ul class="why-list">
    <li><svg width="9" height="7" viewBox="0 0 9 7"><path d="M1 3.5 L3.5 6 L8 1" fill="none" stroke="var(--pink)" stroke-width="1.6"/></svg>Sanfte kurze Bewegungen trainieren<br>Motorik &amp; Koordination</li>
    <li><svg width="9" height="7" viewBox="0 0 9 7"><path d="M1 3.5 L3.5 6 L8 1" fill="none" stroke="var(--pink)" stroke-width="1.6"/></svg>Spielerisch gegen Fatigue für<br>Konzentraion</li>
    <li><svg width="9" height="7" viewBox="0 0 9 7"><path d="M1 3.5 L3.5 6 L8 1" fill="none" stroke="var(--pink)" stroke-width="1.6"/></svg>Freude &amp; Austausch in einer<br>inklusiven Gemeinschaft</li>
  </ul>

  <div class="side-panel"></div>
</body>
</html>
```